Re-Design WP Site BrightPebbles.info

Site Re-design. Also Need a Button for contact on main page. Need Great Looking products re designed. Also bonus if you can install a site SEO checker on the site.

BrightPebbles.info

```html
<!DOCTYPE html>
<html lang="en">
<head>
<meta charset="utf-8">
<title>BrightPebbles.info – Site Re-design</title>
<link href="https://fonts.googleapis.com/css2?family=Poppins:wght@400;500;600&display=swap" rel="stylesheet">
<style>
:root{
  --purple:#5634d6;
  --purple-text:#4a32b8;
  --hero-blue:#2c2ea6;
  --hero-blue-2:#3a3cc2;
  --ink:#1d1d2b;
  --muted:#7a7a8c;
  --line:#e4e4ee;
  --panel:#f4f4f9;
  --sale:#e0322e;
  --gold:#f5b400;
  --white:#ffffff;
}
*{box-sizing:border-box;margin:0;padding:0}
html,body{width:1200px;height:4556px;overflow:hidden}
body{background:var(--white);font-family:"Poppins",sans-serif;color:var(--ink);position:relative}
.page{position:absolute;background:var(--white);box-shadow:0 4px 24px rgba(30,30,60,.12);overflow:hidden}
.page--home{left:152px;top:44px;width:839px;height:1625px}
.page--product{left:146px;top:1761px;width:890px;height:2662px}
.abs{position:absolute}
.section{position:absolute;left:0;width:100%}

/* nav */
.nav{top:0;height:56px;border-bottom:1px solid var(--line);background:var(--white)}
.brand{position:absolute;top:18px;display:flex;align-items:center;gap:6px;font-size:10px;font-weight:500;color:var(--purple-text)}
.brand__dot{width:9px;height:9px;border-radius:50%;background:var(--purple-text)}
.nav__link{position:absolute;top:21px;font-size:9.5px;font-weight:500;color:var(--ink)}
.search{position:absolute;top:16px;height:22px;border:1px solid var(--line);border-radius:4px;font-size:8px;color:var(--muted);padding:5px 0 0 22px}
.search svg{position:absolute;left:7px;top:5px}
.btn{display:inline-block;background:var(--purple);color:var(--white);font-size:8px;font-weight:500;border-radius:3px;text-align:center;line-height:22px;height:22px}
.btn--ghost{background:var(--white);color:var(--ink);border:1px solid var(--line)}
.nav .btn{position:absolute;top:16px}

/* hero */
.hero{top:54px;height:296px;background:linear-gradient(120deg,var(--hero-blue),var(--hero-blue-2))}
.hero__title{left:131px;top:52px;width:260px;color:var(--white);font-size:28px;line-height:34px;font-weight:500}
.hero__text{left:131px;top:127px;width:230px;color:#dcdcfb;font-size:10.5px;line-height:15px}
.hero__cta{left:131px;top:206px;width:108px;height:24px;line-height:24px}
.hero__art{left:406px;top:24px;width:262px;height:238px;border-radius:6px;background:linear-gradient(135deg,#5a5fe0,#3b3fc9 60%,#2a9ee6)}

/* features */
.features{top:350px;height:73px;background:var(--white)}
.feature{position:absolute;top:20px;display:flex;gap:10px;width:190px}
.feature__icon{width:30px;height:30px;border-radius:50%;background:#fbf3dc;flex:none}
.feature h4{font-size:10px;font-weight:600}
.feature p{font-size:7.5px;color:var(--muted);line-height:10px}

/* split */
.split{top:423px;height:518px;background:var(--panel)}
.video{position:absolute;border-radius:2px}
.video--dash{left:131px;top:66px;width:312px;height:178px;background:linear-gradient(#d9d9e2,#a9a9b5)}
.video--seo{left:394px;top:284px;width:314px;height:178px;background:#151518}
.play{position:absolute;left:50%;top:50%;width:24px;height:24px;margin:-12px;border:1.5px solid #fff;border-radius:50%}
.play::after{content:"";position:absolute;left:8px;top:5px;border-left:8px solid #fff;border-top:6px solid transparent;border-bottom:6px solid transparent}
.video__label{position:absolute;left:12px;top:14px;font-size:8px;color:#ccc}
.split__block{position:absolute;width:250px}
.split__block h3{font-size:17px;line-height:22px;font-weight:500;margin-bottom:12px}
.split__block .btn{padding:0 12px}

/* product cards */
.offers{top:941px;height:514px;background:#fafafd}
.card{position:absolute;background:var(--white);border:1px solid var(--line);box-shadow:0 2px 8px rgba(30,30,60,.06)}
.card__img{position:absolute;left:0;top:0;width:100%}
.card__img--screen{background:linear-gradient(#f6d2da,#e84f7a)}
.card__img--aerial{background:linear-gradient(135deg,#8f8f86,#5f6a58)}
.card__img--leaf{background:linear-gradient(135deg,#3e7a2a,#1f4a14)}
.sale{position:absolute;left:0;top:0;background:var(--sale);color:#fff;font-size:7px;font-weight:600;padding:2px 6px}
.card__title{position:absolute;left:10px;right:10px;color:var(--purple-text);font-size:7.5px;line-height:10px;font-weight:500}
.card__price{position:absolute;left:10px;right:10px;font-size:7.5px;line-height:10px}
.card__price s{color:var(--sale)}
.card__price b{font-weight:600}
.card .btn{position:absolute;left:10px;width:60px;height:18px;line-height:18px;font-size:7px}
.card__save{position:absolute;right:12px;width:8px;height:10px;border:1px solid #999;border-bottom:none}
.more{top:422px;width:100%;text-align:center;font-size:8.5px;color:var(--purple-text)}

/* footer */
.footer{background:var(--white)}
.footer__about{position:absolute;font-size:7px;color:var(--muted);line-height:10px;width:110px}
.footer__col{position:absolute;font-size:7.5px;line-height:16px;color:var(--muted)}
.footer__col h5{font-size:8.5px;font-weight:600;color:var(--ink);margin-bottom:6px}

/* product page */
.product-top{top:58px;height:497px}
.product-top__side{position:absolute;left:541px;top:0;width:349px;height:100%;background:var(--panel)}
.crumb{left:152px;top:40px;width:340px;font-size:6.5px;color:var(--muted);line-height:9px;text-transform:uppercase}
.product-title{left:152px;top:80px;width:320px;font-size:14px;line-height:18px;font-weight:500}
.product-img{left:152px;top:146px;width:326px;height:199px;background:linear-gradient(135deg,#eef0fb,#c9d7f2)}
.thumb{position:absolute;top:358px;width:40px;height:40px;border:1px solid var(--line)}
.stars{left:563px;top:46px;color:var(--gold);font-size:16px;letter-spacing:2px}
.price{left:563px;top:80px;width:260px;font-size:14px;line-height:18px;font-weight:500}
.qty{left:563px;top:141px;width:18px;height:18px;border:1px solid var(--line);background:#fff;font-size:7px;text-align:center;line-height:16px}
.product-top .btn{position:absolute;left:593px;top:139px;width:62px}
.side-heading{left:563px;top:190px;width:270px;font-size:13px;line-height:17px;font-weight:500}
.copy{font-size:8px;line-height:15px;color:var(--muted)}
.share{left:431px;top:470px;display:flex;gap:5px;align-items:center;font-size:7px;color:var(--muted)}
.share i{width:14px;height:14px;border:1px solid var(--line);display:block}

.h2{font-size:14px;line-height:18px;font-weight:500}
.feature-row{background:var(--white)}
.slide{position:absolute;top:103px;width:288px;height:162px;background:#0e0f24}
.slide--b{background:#12132a}
.arrow{position:absolute;top:172px;width:24px;height:24px;border:1px solid #999;border-radius:50%}
.arrow svg{position:absolute;left:7px;top:7px}
.checks{position:absolute;top:145px;list-style:none;width:260px}
.checks li{position:relative;padding-left:14px;font-size:8px;line-height:20px;color:var(--muted)}
.checks li::before{content:"";position:absolute;left:0;top:6px;width:7px;height:7px;border:1px solid var(--purple);border-radius:50%}
.cta{top:2316px;height:160px;background:var(--panel)}
</style>
</head>
<body>

<main class="page page--home">
  <header class="section nav">
    <div class="brand" style="left:75px"><span class="brand__dot"></span>BrightPebbles.info</div>
    <span class="nav__link" style="left:206px">Home</span>
    <span class="nav__link" style="left:249px">Shop</span>
    <span class="nav__link" style="left:290px">Solutions</span>
    <span class="nav__link" style="left:349px">Blog</span>
    <div class="search" style="left:399px;width:103px"><svg width="10" height="10" viewBox="0 0 10 10"><circle cx="4" cy="4" r="3" fill="none" stroke="#999"/><path d="M6.5 6.5L9 9" stroke="#999"/></svg>Search</div>
    <span class="btn" style="left:657px;width:59px">Contact Us</span>
    <span class="btn btn--ghost" style="left:734px;width:56px">Sign In</span>
  </header>

  <section class="section hero">
    <h1 class="abs hero__title">We Are Digital Innovators</h1>
    <p class="abs hero__text">We're a studio of creators inventing unique and effective IT applications providing solutions that solve real world problems.</p>
    <span class="abs btn hero__cta">Explore our offering →</span>
    <div class="abs hero__art" role="img" aria-label="Isometric illustration of a person at digital data screens"></div>
  </section>

  <section class="section features">
    <div class="feature" style="left:131px"><span class="feature__icon"></span><div><h4>Based on the results</h4><p>Lorem ipsum Maecenas viverra condimentum nulla</p></div></div>
    <div class="feature" style="left:333px"><span class="feature__icon"></span><div><h4>Problem Solutions</h4><p>Lorem ipsum Maecenas viverra condimentum nulla</p></div></div>
    <div class="feature" style="left:537px"><span class="feature__icon"></span><div><h4>Team of Professional</h4><p>Lorem ipsum Maecenas viverra condimentum nulla</p></div></div>
  </section>

  <section class="section split">
    <div class="video video--dash" role="img" aria-label="Video preview of a search ranking dashboard"><span class="play"></span></div>
    <div class="split__block" style="left:481px;top:66px">
      <h3>Transform your business with the right digital solutions to top local search ranking</h3>
      <span class="btn" style="height:20px;line-height:20px">Contact Us</span>
    </div>
    <div class="split__block" style="left:131px;top:331px">
      <h3>Establishing your business strategy for the digital age</h3>
      <span class="btn" style="height:20px;line-height:20px">Reach with Us</span>
    </div>
    <div class="video video--seo" role="img" aria-label="Video preview explaining what SEO is"><span class="video__label">WHAT IS SEO?</span><span class="play"></span></div>
  </section>

  <section class="section offers">
    <article class="card" style="left:131px;top:51px;width:176px;height:272px">
      <div class="card__img card__img--screen" style="height:174px" role="img" aria-label="Prize display screen promotion"></div><span class="sale">SALE!</span>
      <p class="card__title" style="top:190px">#1 Social Media Marketing! &amp; Local MapSpot Biz Boost – Monthly Prize Included!</p>
      <p class="card__price" style="top:224px"><s>$6,995.00</s> <b>$3,495.00</b> / month and a $500.00 sign-up fee</p>
      <span class="btn" style="top:248px">Sign up now!</span><span class="card__save" style="top:252px"></span>
    </article>
    <article class="card" style="left:332px;top:51px;width:176px;height:272px">
      <div class="card__img card__img--aerial" style="height:174px" role="img" aria-label="Aerial view of a neighbourhood with a geo fence"></div><span class="sale">SALE!</span>
      <p class="card__title" style="top:190px">Digital Marketing – GEO Fence – Track Number of Visitors it Brings to Your Location…</p>
      <p class="card__price" style="top:224px"><s>$1,295.00</s> <b>$895.00</b> / month</p>
      <span class="btn" style="top:248px">Sign up now!</span><span class="card__save" style="top:252px"></span>
    </article>
    <article class="card" style="left:533px;top:51px;width:176px;height:272px">
      <div class="card__img card__img--screen" style="height:174px" role="img" aria-label="Prize display screen promotion"></div><span class="sale">SALE!</span>
      <p class="card__title" style="top:190px">#1 Social Media Marketing &amp; Local MapSpot Biz Boost – Monthly Prize Included!</p>
      <p class="card__price" style="top:224px"><s>$6,995.00</s> <b>$3,495.00</b> / month and a $500.00 sign-up fee</p>
      <span class="btn" style="top:248px">Sign up now!</span><span class="card__save" style="top:252px"></span>
    </article>
    <p class="abs more">More offering →</p>
  </section>

  <footer class="section footer" style="top:1455px;height:170px">
    <div class="brand" style="left:131px;top:34px"><span class="brand__dot"></span>BrightPebbles.info</div>
    <p class="footer__about" style="left:131px;top:58px">We're a studio of creators inventing unique and effective IT applications providing solutions that solve real world problems.</p>
    <div class="footer__col" style="left:310px;top:38px"><h5>Company</h5>About<br>Shop<br>Blog<br>Contact</div>
    <div class="footer__col" style="left:426px;top:38px"><h5>Support</h5>Help and Support<br>FAQs<br>Terms &amp; Conditions<br>Privacy Policy</div>
    <div class="footer__col" style="left:567px;top:38px;line-height:12px"><h5>Get in touch</h5>48 your location Maplebrook,<br>NV 20417<br>Email: support@brightpebbles.info<br>Phone: (000) 555 0142<br><br>© 2022 BrightPebbles. All Rights Reserved.</div>
  </footer>
</main>

<main class="page page--product">
  <header class="section nav" style="height:58px">
    <div class="brand" style="left:80px;top:20px"><span class="brand__dot"></span>BrightPebbles.info</div>
    <span class="nav__link" style="left:218px;top:23px">Home</span>
    <span class="nav__link" style="left:265px;top:23px">Shop</span>
    <span class="nav__link" style="left:307px;top:23px">Solutions</span>
    <span class="nav__link" style="left:370px;top:23px">Blog</span>
    <div class="search" style="left:427px;top:18px;width:105px"><svg width="10" height="10" viewBox="0 0 10 10"><circle cx="4" cy="4" r="3" fill="none" stroke="#999"/><path d="M6.5 6.5L9 9" stroke="#999"/></svg>Search</div>
    <span class="btn" style="left:698px;top:18px;width:63px">Contact Us</span>
    <span class="btn btn--ghost" style="left:774px;top:18px;width:66px">Sign In</span>
  </header>

  <section class="section product-top">
    <div class="product-top__side"></div>
    <p class="abs crumb">Home / #1 Social Media Marketing &amp; Local MapSpot Biz Boost – Monthly Prize Included!</p>
    <h1 class="abs product-title">#1 Social Media Marketing! &amp; Local MapSpot My Biz Boost – Monthly Prize Included!</h1>
    <div class="abs product-img" role="img" aria-label="Illustration of a hand holding a phone with a map pin over a shop street, titled Local Business"></div>
    <span class="abs" style="left:497px;top:150px;width:18px;height:18px;border:1px solid var(--line);border-radius:50%"></span>
    <div class="thumb" style="left:152px" role="img" aria-label="Thumbnail of local business illustration"></div>
    <div class="thumb" style="left:198px;background:#8c1b1b" role="img" aria-label="Thumbnail of product artwork"></div>
    <div class="abs share">Share: <i></i><i></i></div>

    <div class="abs stars">★★★★★</div>
    <p class="abs price">$6,995.00 $3,495.00 / month and a $500.00 sign-up fee</p>
    <span class="abs qty">1</span>
    <span class="btn">Contact Us</span>
    <h2 class="abs side-heading">Powerful Digital PR, SEO, Social Media and Web Presence Technology All-in-One!</h2>
    <p class="abs copy" style="left:563px;top:262px;width:272px">Our MapSpot Biz Boosting platform with included display system &amp; prize program enables us to dramatically increase your social media presence &amp; move your business to page one in Map and Local search rankings and Power fully Maximize your Social Media accounts. Go from 2-3 likes per week to 3-4 likes per Day! Radically RAISE your exposure on social media sites? 200+ posts per month.</p>
  </section>

  <section class="section feature-row" style="top:555px;height:353px;border-top:1px solid var(--line)">
    <h2 class="abs h2" style="left:143px;top:112px;width:300px">Powerful Digital PR, SEO, Social Media and Web Presence Technology All-in-One!</h2>
    <p class="abs copy" style="left:143px;top:165px;width:280px">Our MapSpot Biz Boosting platform with included display system &amp; prize program enables us to dramatically increase your social media presence &amp; move your business to page one in Map and Local search rankings and Power fully Maximize your Social Media accounts. Go from 2-3 likes per week to 3-4 likes per Day! Radically RAISE your exposure on social media sites? 200+ posts per month</p>
    <div class="abs" style="left:464px;top:112px;width:288px;height:218px;border-radius:40px 8px 8px 40px;background:linear-gradient(135deg,#3fe0c0,#3a8ff0 60%,#eef)" role="img" aria-label="Illustration of a hand holding a phone with social icons beside a prize display stand"></div>
  </section>

  <section class="section feature-row" style="top:908px;height:296px">
    <div class="abs" style="left:120px;top:70px;width:295px;height:192px;background:linear-gradient(#ffffff,#e9edf5)" role="img" aria-label="Map pin with rating stars over a city skyline, labelled map ranking"></div>
    <h2 class="abs h2" style="left:464px;top:66px">Get #1 MapSpot Rankings!</h2>
    <p class="abs copy" style="left:464px;top:94px;width:285px">With our Social Marketing program combined with integration of your MapSpot Biz listing into our MapSpot Boosting System pushing your listing will move the needle for page #1 rankings. The typical time to rank is 3-6 months but it can take 6-12 months or longer for highly competitive industries and geographic areas.<br><br>We have a direct MapSpot API integration for map displays of your business listing and a proprietary media room app for one-click publishing and optimization of content on your website. This is a proven solution.</p>
  </section>

  <section class="section feature-row" style="top:1204px;height:286px">
    <h2 class="abs h2" style="left:0;width:100%;top:62px;text-align:center;font-size:13px">Innovative Prize Screen Display!</h2>
    <span class="arrow" style="left:113px"><svg width="9" height="9" viewBox="0 0 9 9"><path d="M6 1L2.5 4.5 6 8" fill="none" stroke="#555"/></svg></span>
    <div class="slide" style="left:150px" role="img" aria-label="Slide: how long does the ranking process take, with a timeline"></div>
    <div class="slide slide--b" style="left:450px" role="img" aria-label="Slide: why map position is key, with statistics"></div>
    <span class="arrow" style="left:752px"><svg width="9" height="9" viewBox="0 0 9 9"><path d="M3 1l3.5 3.5L3 8" fill="none" stroke="#555"/></svg></span>
  </section>

  <section class="section feature-row" style="top:1490px;height:428px">
    <h2 class="abs h2" style="left:0;width:100%;top:70px;text-align:center;font-size:13px">Included With Every Posting Campaign</h2>
    <ul class="checks" style="left:155px">
      <li>At Location Display &amp; Prize System</li>
      <li>MapSpot Rank SEO Package</li>
      <li>Social Media Manager</li>
      <li>Custom Curated Content Showcasing Your Business</li>
      <li>Fresh, Relevant Content Daily to Engage with Your Followers</li>
    </ul>
    <ul class="checks" style="left:441px;width:300px">
      <li>Image Selection/Creation Related to Custom Curated Content</li>
      <li>Consistent Use of Hashtags to Make it Easy for Others to Find You in Social Searches</li>
      <li>Use Of Emojis To Increase Engagement</li>
      <li>Your Choice of Social Media Platforms</li>
      <li>Unlimited Support</li>
    </ul>
    <p class="abs copy" style="left:245px;top:306px;width:400px;text-align:center;text-transform:uppercase;font-size:7.5px">Plus six social media platforms – 6 posting 365 days a year! Daily engage your followers with 200 posts of relevant current content created specifically for your target audience.</p>
  </section>

  <h2 class="abs h2" style="left:155px;top:1918px">Related products</h2>
  <article class="card" style="left:155px;top:1950px;width:190px;height:331px">
    <div class="card__img card__img--screen" style="height:183px" role="img" aria-label="Prize display screen promotion"></div><span class="sale">SALE!</span>
    <p class="card__title" style="top:205px">#1 Social Media Marketing! &amp; Local MapSpot My Biz Boost – Monthly Prize Included!</p>
    <p class="card__price" style="top:243px"><s>$6,995.00</s> <b>$3,495.00</b> / month and a $500.00 sign-up fee</p>
    <span class="btn" style="top:293px">Sign up now!</span><span class="card__save" style="top:297px"></span>
  </article>
  <article class="card" style="left:369px;top:1950px;width:190px;height:331px">
    <div class="card__img card__img--aerial" style="height:183px" role="img" aria-label="Aerial view of a neighbourhood with a geo fence"></div><span class="sale">SALE!</span>
    <p class="card__title" style="top:205px">Digital Marketing – GEO Fence – Track Number of Visitors it Brings to Your Location…</p>
    <p class="card__price" style="top:243px"><s>$1,295.00</s> <b>$895.00</b> / month</p>
    <span class="btn" style="top:293px">Sign up now!</span><span class="card__save" style="top:297px"></span>
  </article>
  <article class="card" style="left:582px;top:1950px;width:190px;height:331px">
    <div class="card__img card__img--leaf" style="height:183px" role="img" aria-label="Plant leaves behind a prize display screen"></div><span class="sale">SALE!</span>
    <p class="card__title" style="top:205px">#1 Cannabis Advertising w/GEO Fence! Social Media Marketing! &amp; Local SEO MapSpot My…</p>
    <p class="card__price" style="top:243px"><s>$6,995.00</s> <b>$3,495.00</b> / month and a $500.00 sign-up fee</p>
    <span class="btn" style="top:293px">Sign up now!</span><span class="card__save" style="top:297px"></span>
  </article>

  <section class="section cta">
    <h2 class="abs" style="left:0;width:100%;top:54px;text-align:center;font-size:19px;font-weight:500">Get in contact with our expert team today</h2>
    <span class="abs btn" style="left:414px;top:100px;width:62px">Contact Us</span>
  </section>

  <footer class="section footer" style="top:2476px;height:186px">
    <div class="brand" style="left:138px;top:32px"><span class="brand__dot"></span>BrightPebbles.info</div>
    <p class="footer__about" style="left:138px;top:56px">We're a studio of creators inventing unique and effective IT applications providing solutions that solve real world problems.</p>
    <div class="footer__col" style="left:328px;top:38px"><h5>Company</h5>About<br>Shop<br>Blog<br>Contact</div>
    <div class="footer__col" style="left:450px;top:38px"><h5>Support</h5>Help and Support<br>FAQs<br>Terms &amp; Conditions<br>Privacy Policy</div>
    <div class="footer__col" style="left:600px;top:38px;line-height:12px"><h5>Get in touch</h5>48 your location Maplebrook,<br>NV 20417<br>Email: support@brightpebbles.info<br>Phone: (000) 555 0142<br><br>© 2022 BrightPebbles. All Rights Reserved.</div>
  </footer>
</main>

</body>
</html>
```